Heron Freightways LLC needs a web desigh ASAP!

We need a fully functioning web site for our trucking company!
we currently have our domain and logo.
Attached you will find our logo files and word documents with info we would like to include in our web page. (Navigation Tabs and dropdown menu)
Our domain is heronfreightways.net (from webnestly)
Our Chatterbook page is Heron Freightways LLC. You can find pictures and a little bit about our company.
our original logo is the one with bull on the left side.
Our trucking company is based in south Texas, but travel within the USA and Canada.

Target Market(s)

Logistic
Refrigerated Fleet Clients
Transportation
Trucking companies

Industry/Entity Type

Trucking Company

Coding

Coded - Design and coding required

Number of Pages Required

1 page

Font styles to use
Sans Serif

Colors
f04a51
3277b5
ffffff

Requirements
Must have
• our main email contact is Info@heronfreightways.net
• we would like see the colors of our logo. it would be nice to have a truck with our logo in the background.
• We need a web site that we can manage on our own easily.
Nice to have
• roads, highways
• get a quote module
• our inspirational web pages are:
• www.marwickhaulage.com
• www.dorvelcargo.com
• we are open to use stock photos

```html
<!DOCTYPE html>
<html lang="en">
<head>
<meta charset="utf-8">
<title>Heron Freightways LLC</title>
<link href="https://fonts.googleapis.com/css2?family=Bebas+Neue&family=Open+Sans:wght@300;400;600;700&display=swap" rel="stylesheet">
<style>
:root{
  --red:#b8131d;
  --navy:#0a2a55;
  --white:#ffffff;
  --light:#efefef;
  --text:#555555;
  --footer:#333333;
  --footer-text:#dddddd;
  --field:#f3f3f3;
  --field-line:#cfcfcf;
}
*{box-sizing:border-box;margin:0;padding:0}
html,body{width:1200px;height:2663px;overflow:hidden}
body{font-family:"Open Sans",Arial,sans-serif;color:var(--text);background:var(--white)}
.wrap{width:1044px;margin:0 auto;position:relative}

/* header */
.site-header{height:135px;background:var(--white)}
.site-header .wrap{display:flex;justify-content:space-between;align-items:center;height:135px}
.brand{display:flex;align-items:center;gap:14px}
.brand-dot{width:26px;height:26px;border-radius:50%;background:var(--red)}
.brand-name{font-weight:700;font-size:38px;color:var(--navy);letter-spacing:-0.5px}
.tollfree{display:flex;align-items:center;gap:14px}
.tollfree-icon{width:62px;height:62px;border-radius:50%;background:var(--red);display:flex;align-items:center;justify-content:center}
.tollfree-label{font-size:22px;color:var(--navy);line-height:1.1}
.tollfree-number{font-size:33px;font-weight:700;color:var(--red);line-height:1.15}

/* nav */
.main-nav{height:57px;background:var(--navy)}
.main-nav ul{list-style:none;display:flex;height:57px}
.main-nav li{display:flex;align-items:center;padding:0 31px;font-size:19px;color:var(--white);text-transform:uppercase}
.main-nav li.active{background:var(--red);width:137px;justify-content:center;padding:0}

/* hero */
.hero{position:relative;height:573px;overflow:hidden}
.hero-photo{position:absolute;inset:0;background:
  radial-gradient(ellipse 420px 220px at 330px 300px,rgba(240,242,243,.9),rgba(240,242,243,0) 100%),
  linear-gradient(180deg,#6d7270 0%,#c9cdcb 38%,#dfe2e0 55%,#8a8c88 72%,#3c3d3a 100%)}
.hero-copy{position:absolute;right:71px;top:172px;text-align:right}
.hero-title{font-family:"Bebas Neue",Arial,sans-serif;font-size:60px;line-height:62px;color:var(--navy);font-weight:400;letter-spacing:0}
.btn{display:inline-block;font-family:"Open Sans",Arial,sans-serif;color:var(--white);text-transform:uppercase;text-align:center}
.btn-red{background:var(--red)}
.btn-navy{background:var(--navy)}
.hero-btn{position:absolute;right:78px;top:330px;width:204px;height:61px;line-height:61px;font-size:27px}

/* welcome */
.welcome{height:520px;background:var(--light)}
.welcome .wrap{display:flex;justify-content:space-between}
.welcome-copy{width:640px;padding-top:66px}
.welcome-title{font-size:36px;font-weight:400;color:var(--red);line-height:1.2;margin-bottom:12px;white-space:nowrap}
.welcome-title span{color:var(--navy)}
.welcome-copy p{font-size:16px;line-height:25px;margin-bottom:24px;width:610px}
.read-more{width:174px;height:52px;line-height:52px;font-size:23px;margin-top:4px}
.quote-box{width:364px;height:392px;margin-top:60px;background:var(--white)}
.quote-head{height:78px;background:var(--red);clip-path:polygon(0 0,100% 0,100% 80%,0 100%);color:var(--white);font-size:31px;padding:10px 0 0 40px}
.quote-form{padding:0 16px;display:flex;flex-direction:column;align-items:center}
.field{width:334px;height:36px;background:var(--field);border:1px solid var(--field-line);font-size:15px;color:#666;padding:7px 9px;margin-bottom:10px}
.field-message{height:82px}
.submit{width:146px;height:52px;line-height:52px;font-size:23px;margin-top:3px}

/* services */
.services{position:relative;height:581px;overflow:hidden;color:var(--white)}
.services-bg{position:absolute;inset:0;background:linear-gradient(120deg,#0b2a55 0%,#1d4474 45%,#12335f 65%,#0a2349 100%)}
.services .wrap{text-align:center;padding-top:53px}
.section-title{font-size:39px;font-weight:400;line-height:1.2}
.services-intro{font-size:16px;line-height:25px;width:820px;margin:10px auto 0}
.service-grid{display:flex;justify-content:space-between;margin-top:38px}
.service{width:322px}
.service-photo{height:187px}
.photo-canada{background:linear-gradient(180deg,#b8383a 0%,#c95a55 50%,#a8443e 100%)}
.photo-usa{background:linear-gradient(180deg,#5a6494 0%,#b9a8b6 55%,#b8545a 100%)}
.photo-fleet{background:linear-gradient(180deg,#a9c4dc 0%,#e8edf0 45%,#c9cbc7 75%,#8b8a82 100%)}
.service-title{font-size:26px;font-weight:400;margin-top:14px;line-height:1.2;text-transform:uppercase}
.service p{font-size:16px;line-height:25px;margin-top:6px}

/* jobs */
.jobs{height:312px;background:var(--red);color:var(--white)}
.jobs .wrap{padding-top:38px}
.jobs .section-title{text-align:center;font-weight:300;font-size:40px}
.job-list{display:flex;margin-top:16px;position:relative}
.job-list::after{content:"";position:absolute;left:522px;top:0;width:1px;height:156px;background:rgba(255,255,255,.45)}
.job{display:flex;width:560px;gap:22px}
.job + .job{width:484px}
.job-badge{flex:none;width:124px;height:124px;border-radius:50%;background:var(--white);display:flex;align-items:center;justify-content:center}
.job-icon{width:58px;height:52px;background:var(--navy);border-radius:6px}
.job-title{font-size:32px;font-weight:400;margin-top:4px;line-height:1.3}
.job p{font-size:16px;line-height:25px;margin-top:6px;width:340px}

/* call to action */
.cta{height:137px;background:var(--white)}
.cta .wrap{display:flex;justify-content:space-between;align-items:center;height:137px}
.cta-title{font-family:"Bebas Neue",Arial,sans-serif;font-size:47px;color:var(--navy);font-weight:400;letter-spacing:.5px}
.cta-btn{width:185px;height:52px;line-height:52px;font-size:23px}

/* footer */
.site-footer{height:348px;background:var(--footer);color:var(--footer-text)}
.footer-cols{display:flex;padding-top:38px;height:277px;border-bottom:1px solid #555}
.footer-col{font-size:15px;line-height:25px}
.col-about{width:270px}
.col-links{width:272px}
.col-news{width:269px}
.col-contact{width:233px}
.footer-brand{font-size:23px;font-weight:700;color:var(--white);margin:8px 0 16px;line-height:1.1}
.footer-col h3{font-size:23px;font-weight:400;color:var(--white);margin-bottom:14px}
.footer-col p{width:225px}
.links{list-style:none}
.links li{display:flex;align-items:center;gap:8px;font-size:17px;line-height:31px;color:var(--white)}
.news-item{width:230px;padding-bottom:10px;margin-bottom:10px;border-bottom:1px solid #555}
.news-item:last-child{border:none}
.news-date{display:flex;align-items:center;gap:6px;font-size:13px;color:#999;margin-top:2px}
.contact-row{display:flex;gap:14px;margin-bottom:16px;align-items:flex-start}
.contact-row svg{flex:none;margin-top:4px}
.footer-bottom{display:flex;justify-content:space-between;align-items:center;height:70px}
.copyright{font-size:14px;color:var(--white)}
.social{display:flex;align-items:center;gap:18px;font-size:21px;color:var(--white);text-transform:uppercase}
.social-dot{width:44px;height:44px;border-radius:50%;background:var(--red)}
</style>
</head>
<body>

<header class="site-header">
  <div class="wrap">
    <div class="brand">
      <span class="brand-dot"></span>
      <span class="brand-name">Heron Freightways</span>
    </div>
    <div class="tollfree">
      <div class="tollfree-icon">
        <svg width="30" height="30" viewBox="0 0 24 24"><path fill="#fff" d="M6.6 10.8a15.1 15.1 0 0 0 6.6 6.6l2.2-2.2c.3-.3.7-.4 1-.2 1.1.4 2.3.6 3.6.6.6 0 1 .4 1 1V20c0 .6-.4 1-1 1A17 17 0 0 1 3 4c0-.6.4-1 1-1h3.5c.6 0 1 .4 1 1 0 1.3.2 2.5.6 3.6.1.3 0 .7-.2 1z"/></svg>
      </div>
      <div>
        <div class="tollfree-label">Toll Free Number</div>
        <div class="tollfree-number">1-884-555-0147</div>
      </div>
    </div>
  </div>
</header>

<nav class="main-nav">
  <div class="wrap">
    <ul>
      <li class="active">Home</li>
      <li>About</li>
      <li>Services</li>
      <li>Career</li>
      <li>News</li>
      <li>Contact</li>
    </ul>
  </div>
</nav>

<section class="hero">
  <div class="hero-photo" role="img" aria-label="White refrigerated truck driving on a motion-blurred highway under a cloudy grey sky"></div>
  <div class="hero-copy">
    <h1 class="hero-title">Your Total<br>Transportation Partner.</h1>
  </div>
  <span class="btn btn-red hero-btn">Contact Us</span>
</section>

<section class="welcome">
  <div class="wrap">
    <div class="welcome-copy">
      <h2 class="welcome-title">WELCOME TO <span>HERON FREIGHTWAYS</span></h2>
      <p>We carry and deliver almost any type of temperature sensitive products anywhere in the United States.</p>
      <p>Heron Freightways LLC currently has the very latest in transport refrigeration technology. Our brand new trucks and professional-looking equipment set the standard with outstanding efficiency and reliability paired with superior temperature control.</p>
      <p>We offer quality and reliability. We've got you and your business covered day and night, from origin to destination.</p>
      <span class="btn btn-navy read-more">Read More</span>
    </div>
    <aside class="quote-box">
      <div class="quote-head">GET A FREE QUOTE</div>
      <div class="quote-form">
        <div class="field">Enter Name</div>
        <div class="field">Enter Email</div>
        <div class="field">Enter Contact No.</div>
        <div class="field field-message">Enter Message</div>
        <span class="btn btn-navy submit">Submit</span>
      </div>
    </aside>
  </div>
</section>

<section class="services">
  <div class="services-bg" role="img" aria-label="Dark blue tinted photo of trucks at a loading dock"></div>
  <div class="wrap">
    <h2 class="section-title">SERVICES WE PROVIDE</h2>
    <p class="services-intro">We carry and deliver almost any type of temperature sensitive products anywhere in the United States. Heron Freightways LLC currently has the very latest in transport refrigeration technology.</p>
    <div class="service-grid">
      <article class="service">
        <div class="service-photo photo-canada" role="img" aria-label="Photo of the Canadian flag painted on weathered wood"></div>
        <h3 class="service-title">Canada Service</h3>
        <p>Lorem Ipsum is simply dummy text of the printing and typesetting industry. Lorem Ipsum has been the industry.</p>
      </article>
      <article class="service">
        <div class="service-photo photo-usa" role="img" aria-label="Photo of the American flag waving"></div>
        <h3 class="service-title">USA Service</h3>
        <p>Lorem Ipsum is simply dummy text of the printing and typesetting industry. Lorem Ipsum has been the industry.</p>
      </article>
      <article class="service">
        <div class="service-photo photo-fleet" role="img" aria-label="Row of white semi trucks parked in a yard"></div>
        <h3 class="service-title">Refrigerated</h3>
        <p>Lorem Ipsum is simply dummy text of the printing and typesetting industry. Lorem Ipsum has been the industry.</p>
      </article>
    </div>
  </div>
</section>

<section class="jobs">
  <div class="wrap">
    <h2 class="section-title">JOB OPENING</h2>
    <div class="job-list">
      <article class="job">
        <div class="job-badge"><div class="job-icon" role="img" aria-label="Forklift icon"></div></div>
        <div>
          <h3 class="job-title">Drivers</h3>
          <p>We are currently hiring CDL Truck Drivers. Must have 2 year minimum experience and a clean driving record.</p>
        </div>
      </article>
      <article class="job">
        <div class="job-badge"><div class="job-icon" role="img" aria-label="Office worker at a desk icon"></div></div>
        <div>
          <h3 class="job-title">Office Clerk</h3>
          <p>We are looking for a competent Office Clerk to perform various administrative and clerical tasks and duties in an office setting.</p>
        </div>
      </article>
    </div>
  </div>
</section>

<section class="cta">
  <div class="wrap">
    <h2 class="cta-title">Not sure which solution fits your business needs?</h2>
    <span class="btn btn-navy cta-btn">Contact Us</span>
  </div>
</section>

<footer class="site-footer">
  <div class="wrap">
    <div class="footer-cols">
      <div class="footer-col col-about">
        <div class="footer-brand">Heron Freightways</div>
        <p>We carry and deliver almost any type of temperature sensitive products anywhere in the United States.</p>
      </div>
      <div class="footer-col col-links">
        <h3>Useful Links</h3>
        <ul class="links">
          <li><svg width="14" height="14" viewBox="0 0 14 14"><circle cx="7" cy="7" r="5.5" fill="none" stroke="#fff" stroke-width="1.6"/><circle cx="7" cy="7" r="2.2" fill="#fff"/></svg>Home</li>
          <li><svg width="14" height="14" viewBox="0 0 14 14"><circle cx="7" cy="7" r="5.5" fill="none" stroke="#fff" stroke-width="1.6"/><circle cx="7" cy="7" r="2.2" fill="#fff"/></svg>About</li>
          <li><svg width="14" height="14" viewBox="0 0 14 14"><circle cx="7" cy="7" r="5.5" fill="none" stroke="#fff" stroke-width="1.6"/><circle cx="7" cy="7" r="2.2" fill="#fff"/></svg>Services</li>
          <li><svg width="14" height="14" viewBox="0 0 14 14"><circle cx="7" cy="7" r="5.5" fill="none" stroke="#fff" stroke-width="1.6"/><circle cx="7" cy="7" r="2.2" fill="#fff"/></svg>Career</li>
          <li><svg width="14" height="14" viewBox="0 0 14 14"><circle cx="7" cy="7" r="5.5" fill="none" stroke="#fff" stroke-width="1.6"/><circle cx="7" cy="7" r="2.2" fill="#fff"/></svg>News</li>
          <li><svg width="14" height="14" viewBox="0 0 14 14"><circle cx="7" cy="7" r="5.5" fill="none" stroke="#fff" stroke-width="1.6"/><circle cx="7" cy="7" r="2.2" fill="#fff"/></svg>Contact</li>
        </ul>
      </div>
      <div class="footer-col col-news">
        <h3>Latest News</h3>
        <div class="news-item">
          <div>Lorem Ipsum is simply dummy text of the printing.</div>
          <div class="news-date"><svg width="12" height="12" viewBox="0 0 12 12"><rect x="1" y="2" width="10" height="9" fill="none" stroke="#999" stroke-width="1.2"/><rect x="1" y="2" width="10" height="3" fill="#999"/></svg>29 August 2016</div>
        </div>
        <div class="news-item">
          <div>Lorem Ipsum is simply dummy text of the printing.</div>
          <div class="news-date"><svg width="12" height="12" viewBox="0 0 12 12"><rect x="1" y="2" width="10" height="9" fill="none" stroke="#999" stroke-width="1.2"/><rect x="1" y="2" width="10" height="3" fill="#999"/></svg>29 August 2016</div>
        </div>
      </div>
      <div class="footer-col col-contact">
        <h3>Get In Touch</h3>
        <div class="contact-row">
          <svg width="16" height="20" viewBox="0 0 16 20"><path fill="#fff" d="M8 0a7 7 0 0 0-7 7c0 5 7 13 7 13s7-8 7-13a7 7 0 0 0-7-7zm0 10a3 3 0 1 1 0-6 3 3 0 0 1 0 6z"/></svg>
          <div>4410 N. Palm Blvd.<br>Alton, TX 78573</div>
        </div>
        <div class="contact-row">
          <svg width="18" height="18" viewBox="0 0 24 24"><path fill="#fff" d="M6.6 10.8a15.1 15.1 0 0 0 6.6 6.6l2.2-2.2c.3-.3.7-.4 1-.2 1.1.4 2.3.6 3.6.6.6 0 1 .4 1 1V20c0 .6-.4 1-1 1A17 17 0 0 1 3 4c0-.6.4-1 1-1h3.5c.6 0 1 .4 1 1 0 1.3.2 2.5.6 3.6.1.3 0 .7-.2 1z"/></svg>
          <div>1-884-555-0147</div>
        </div>
        <div class="contact-row">
          <svg width="18" height="14" viewBox="0 0 18 14"><rect x="1" y="1" width="16" height="12" rx="1.5" fill="none" stroke="#fff" stroke-width="1.6"/><path d="M1.5 2l7.5 6 7.5-6" fill="none" stroke="#fff" stroke-width="1.6"/></svg>
          <div>marcoruiz@heronfreightw<br>ays.net</div>
        </div>
      </div>
    </div>
    <div class="footer-bottom">
      <div class="copyright">© <strong>Heron Freightways</strong> - 2016. All Rights Reserved.</div>
      <div class="social"><span class="social-dot"></span>Follow us on Chatterbook</div>
    </div>
  </div>
</footer>

</body>
</html>
```